Ferris Contracting LLC Business Card Design

I am looking for a creative and unique business card design. We are a commercial construction general contractor. With the name "FERRIS" Contracting, I am hoping to see some neat designs that correlate with the name.

```html
<!DOCTYPE html>
<html lang="en">
<head>
<meta charset="utf-8">
<title>Ferris Contracting LLC – Business Card</title>
<link rel="stylesheet" href="https://fonts.googleapis.com/css2?family=Poppins:wght@400;600;700&display=swap">
<style>
  :root {
    --stage: #808080;
    --card-dark: #0b0b0b;
    --card-dark-soft: #1c1c1c;
    --card-light: #ffffff;
    --brand-blue: #1f8ad6;
    --name-blue: #175f95;
    --ink: #222222;
    --rule: #9a9a9a;
    --white: #ffffff;
  }
  * { margin: 0; padding: 0; box-sizing: border-box; }
  html, body {
    width: 1119px; height: 1200px; overflow: hidden;
    background: var(--stage);
    font-family: "Poppins", sans-serif;
  }
  .card {
    position: absolute; left: 94px; width: 844px; height: 482px;
    box-shadow: 4px 6px 12px rgba(0,0,0,0.35);
    overflow: hidden;
  }
  .card--front { top: 70px; }
  .card--back  { top: 601px; display: flex; }

  .dark-surface {
    background: radial-gradient(ellipse at 50% 35%, var(--card-dark-soft) 0%, var(--card-dark) 75%);
  }

  .brand-name {
    position: absolute;
    color: var(--brand-blue);
    font-weight: 700;
    white-space: nowrap;
    letter-spacing: 0.04em;
    line-height: 1;
  }
  .card--front .brand-name {
    left: 0; right: 0; top: 200px; text-align: center; font-size: 46px;
  }
  .front-url {
    position: absolute; left: 0; right: 0; top: 448px;
    text-align: center; font-size: 29px; font-weight: 700;
    letter-spacing: 0.04em; color: var(--white); line-height: 1;
  }
  .front-url .domain { color: var(--brand-blue); }

  .back-brand { position: relative; width: 385px; height: 100%; }
  .back-brand .brand-name {
    left: 0; right: 0; top: 227px; text-align: center; font-size: 27px;
  }

  .back-details {
    position: relative; flex: 1; background: var(--card-light);
    padding: 130px 0 0 42px;
  }
  .person-name {
    font-size: 46px; font-weight: 700; color: var(--name-blue);
    line-height: 1.1; letter-spacing: -0.005em;
  }
  .name-rule {
    width: 332px; height: 1px; background: var(--rule); margin: 8px 0 10px 0;
  }
  .person-title {
    font-size: 15px; font-weight: 600; color: var(--ink); margin-left: 3px;
  }
  .contact-list {
    position: relative; list-style: none; margin-top: 30px;
  }
  .contact-list::before {
    content: ""; position: absolute; left: 10px; top: 12px; bottom: 12px;
    width: 2px; background: var(--name-blue);
  }
  .contact-item {
    position: relative; display: flex; align-items: flex-start;
    font-size: 19.5px; color: var(--ink); line-height: 24px;
    margin-bottom: 7px; letter-spacing: 0.02em;
  }
  .contact-icon {
    position: relative; flex: none; width: 22px; height: 22px;
    margin-right: 12px; margin-top: 1px;
  }
</style>
</head>
<body>

  <section class="card card--front dark-surface">
    <div class="brand-name">FERRIS CONTRACTING</div>
    <div class="front-url">www.<span class="domain">ferriscontractingusa</span>.com</div>
  </section>

  <section class="card card--back">
    <div class="back-brand dark-surface">
      <div class="brand-name">FERRIS CONTRACTING</div>
    </div>

    <div class="back-details">
      <h1 class="person-name">Dylan Marsh</h1>
      <div class="name-rule"></div>
      <p class="person-title">State-licensed general contractor</p>

      <ul class="contact-list">
        <li class="contact-item">
          <svg class="contact-icon" viewBox="0 0 22 22" aria-hidden="true">
            <circle cx="11" cy="11" r="11" fill="#175f95"/>
            <path d="M7.5 5.5l2 0 1 3-1.4 1.1a7 7 0 0 0 3.3 3.3l1.1-1.4 3 1v2a1.5 1.5 0 0 1-1.6 1.5A10 10 0 0 1 6 7.1 1.5 1.5 0 0 1 7.5 5.5z" fill="#fff"/>
          </svg>
          <span>816-555-0173</span>
        </li>
        <li class="contact-item">
          <svg class="contact-icon" viewBox="0 0 22 22" aria-hidden="true">
            <circle cx="11" cy="11" r="11" fill="#175f95"/>
            <rect x="5.5" y="7" width="11" height="8" fill="#fff"/>
            <path d="M5.5 7l5.5 4.5L16.5 7" fill="none" stroke="#175f95" stroke-width="1.2"/>
          </svg>
          <span>2740 East Holloway Rd<br>Lee's Summit, MO 64063</span>
        </li>
        <li class="contact-item">
          <svg class="contact-icon" viewBox="0 0 22 22" aria-hidden="true">
            <circle cx="11" cy="11" r="11" fill="#175f95"/>
            <g fill="none" stroke="#fff" stroke-width="1.1">
              <circle cx="11" cy="11" r="6"/>
              <ellipse cx="11" cy="11" rx="2.6" ry="6"/>
              <path d="M5 11h12M6 8h10M6 14h10"/>
            </g>
          </svg>
          <span>www.ferriscontractingusa.com</span>
        </li>
      </ul>
    </div>
  </section>

</body>
</html>
```